Professional Modern Website Design

We are a premium IT services provider to the financial industry based in London. Our company is called Norquell our current holding page is www.norquell-example.co.uk. We require a new website to match our new corporate identity. This project is for the design phase only. Development will be handled in-house. I have attached examples of wire frames we have developed (although open to suggestions for improvement) Our brand document that should demonstrate current brand, inc how we communicate to potential clients and finally mostly completed web-content.
We are looking for designers that can create something that sets us apart from our competitors.
Target Market(s)
IT Decision makers in Finance companies such as; hedge funds, private investment banks etc
Industry/Entity Type
Financial
Number of Pages Required
5+ page
Requirements
Must have
- hexagon elements in the design, unique design.
Nice to have
- Blog and social media feeds
Should not have
- Should not resemble a downloaded template

```html
<!DOCTYPE html>
<html lang="en">
<head>
<meta charset="utf-8">
<title>Norquell — Systems Integration for Finance</title>
<link href="https://fonts.googleapis.com/css2?family=Dosis:wght@300;400;500;600&family=Open+Sans:wght@300;400;600;700&display=swap" rel="stylesheet">
<style>
  :root {
    --orange: #f5801f;
    --orange-deep: #f26522;
    --ink: #2b2b2b;
    --nav-bg: #111111;
    --card-line: #9a9a9a;
    --btn-dark: #3a3a3a;
    --white: #ffffff;
    --footer-bar: #2a2a2a;
  }
  * { box-sizing: border-box; margin: 0; padding: 0; }
  html, body { width: 825px; height: 1200px; overflow: hidden; background: var(--white); }
  body { position: relative; font-family: "Open Sans", Arial, sans-serif; color: var(--ink); }
  .abs { position: absolute; }

  /* Top navigation */
  .topbar { left: 0; top: 0; width: 825px; height: 34px; background: var(--nav-bg); z-index: 3; }
  .brand-mark { left: 82px; top: 9px; font-family: "Open Sans", sans-serif; font-weight: 700; font-size: 12px; color: var(--orange); }
  .main-nav { left: 0; width: 825px; top: 11px; display: flex; justify-content: center; gap: 19px; font-family: "Dosis", sans-serif; font-size: 11px; letter-spacing: .6px; color: var(--white); padding-left: 12px; }
  .main-nav .active { color: var(--orange); }
  .social-row { left: 675px; top: 9px; display: flex; gap: 2px; }

  /* Hero */
  .hero { left: 0; top: 34px; width: 825px; height: 392px; background: linear-gradient(180deg, #3a3a3a 0%, #262626 45%, #1b1b1b 100%); }
  .hero-brand { left: 0; width: 825px; top: 164px; text-align: center; font-family: "Open Sans", sans-serif; font-weight: 300; font-size: 13px; letter-spacing: 6px; color: #dddddd; }
  .hero-title { left: 0; width: 825px; top: 204px; text-align: center; font-family: "Dosis", sans-serif; font-weight: 300; font-size: 20px; color: var(--white); }
  .hero-lead { left: 160px; width: 505px; top: 230px; text-align: center; font-size: 10px; line-height: 12.5px; color: var(--white); }
  .hero-lead em { font-style: normal; color: var(--orange); }
  .hero-call { left: 0; width: 825px; top: 285px; text-align: center; font-family: "Dosis", sans-serif; font-size: 12px; color: var(--white); }
  .hero-call strong { font-weight: 600; font-size: 13px; }
  .btn-primary { left: 362px; top: 320px; width: 100px; height: 26px; background: var(--orange-deep); color: var(--white); font-family: "Dosis", sans-serif; font-size: 13px; letter-spacing: .5px; display: flex; align-items: center; justify-content: center; }
  .slider-dots { left: 393px; top: 380px; display: flex; gap: 3px; }
  .slider-dots span { width: 8px; height: 8px; border-radius: 50%; border: 1.2px solid var(--white); }
  .slider-dots .on { background: var(--white); }

  /* About */
  .section-title { left: 0; width: 825px; top: 476px; text-align: center; font-family: "Dosis", sans-serif; font-weight: 300; font-size: 26px; color: #444; }
  .section-lead { left: 150px; width: 525px; top: 514px; text-align: center; font-size: 10.5px; line-height: 13px; color: #222; }

  .role-card { top: 580px; width: 152px; height: 285px; border: 1.5px solid var(--card-line); background: var(--white); text-align: center; }
  .role-card.featured { background: var(--orange); border-color: var(--orange); color: var(--white); }
  .role-card svg { position: absolute; left: 29px; top: 33px; }
  .role-name { position: absolute; left: 0; width: 100%; top: 156px; font-size: 10.5px; color: #222; }
  .featured .role-name { font-weight: 700; color: var(--white); }
  .role-text { position: absolute; left: 14px; right: 14px; top: 176px; font-size: 8.3px; line-height: 10px; color: #222; }
  .featured .role-text { color: var(--white); }
  .role-btn { position: absolute; left: 47px; top: 226px; width: 58px; height: 16px; background: var(--btn-dark); color: var(--white); font-size: 6.5px; display: flex; align-items: center; justify-content: center; }
  .featured .role-btn { left: 47px; width: 59px; background: var(--white); }

  /* Footer */
  .footer { left: 0; top: 947px; width: 825px; height: 253px; background: linear-gradient(100deg, #2c2c2c 0%, #4a4a4a 40%, #6a6a6a 70%, #3a3a3a 100%); }
  .footer-brand { left: 82px; top: 1062px; font-weight: 700; font-size: 17px; color: var(--orange); }
  .footer-links { list-style: none; font-family: "Dosis", sans-serif; font-size: 10px; line-height: 15.5px; color: var(--white); }
  .footer-links li::before { content: "›"; margin-right: 4px; }
  .field { border: 1px solid #e5e5e5; color: var(--white); font-size: 8.5px; padding: 8px 11px; }
  .btn-send { left: 391px; top: 1094px; width: 82px; height: 28px; border: 1px solid #e5e5e5; color: var(--white); font-family: "Dosis", sans-serif; font-size: 13px; display: flex; align-items: center; justify-content: center; }
  .copyright { left: 0; top: 1167px; width: 825px; height: 33px; background: var(--footer-bar); color: var(--white); font-size: 8.5px; display: flex; align-items: center; justify-content: center; }
</style>
</head>
<body>

<header class="abs topbar">
  <div class="abs brand-mark">Norquell</div>
  <nav class="abs main-nav">
    <span>ABOUT</span><span class="active">SERVICES</span><span>PARTNER</span><span>CLIENTS</span><span>CONTACT</span>
  </nav>
  <div class="abs social-row" aria-label="Social links">
    <svg width="17" height="18" viewBox="0 0 17 18"><polygon points="8.5,1 16,5 16,13 8.5,17 1,13 1,5" fill="#f5801f"/></svg>
    <svg width="17" height="18" viewBox="0 0 17 18"><polygon points="8.5,1 16,5 16,13 8.5,17 1,13 1,5" fill="none" stroke="#fff"/></svg>
    <svg width="17" height="18" viewBox="0 0 17 18"><polygon points="8.5,1 16,5 16,13 8.5,17 1,13 1,5" fill="none" stroke="#fff"/></svg>
    <svg width="17" height="18" viewBox="0 0 17 18"><polygon points="8.5,1 16,5 16,13 8.5,17 1,13 1,5" fill="none" stroke="#fff"/></svg>
  </div>
</header>

<section class="abs hero" role="img" aria-label="Black and white night skyline of a waterfront financial district"></section>
<div class="abs hero-brand">NORQUELL</div>
<h1 class="abs hero-title">YOU NEED INTEGRATION. WE'RE INVISIBLE BUT ALWAYS SUPPORTING YOU.</h1>
<p class="abs hero-lead"><em>Norquell</em> is one of the leading systems integrators to the world's finance sector. We are an extension of your business and our services portfolio has been built so you always have access to a complete partner.</p>
<p class="abs hero-call">Call us today : <strong>1800 000 147</strong></p>
<div class="abs btn-primary">LEARN MORE</div>
<div class="abs slider-dots"><span></span><span class="on"></span><span></span><span></span></div>

<h2 class="abs section-title">Who we are ?</h2>
<p class="abs section-lead">If you're working a financial organisation, we have the servies to help everyone in your organisation work more efficiently, productively and profitably.</p>

<article class="abs role-card featured" style="left:82px">
  <svg width="94" height="108" viewBox="0 0 94 108">
    <polygon points="47,2 92,28 92,80 47,106 2,80 2,28" fill="#fff"/>
    <g fill="none" stroke="#f5801f" stroke-width="2">
      <polyline points="30,40 30,70 64,70"/>
      <polyline points="34,60 43,50 50,55 62,42"/>
      <polyline points="56,42 62,42 62,48"/>
    </g>
    <g fill="#f5801f"><rect x="36" y="60" width="4" height="10"/><rect x="43" y="56" width="4" height="14"/><rect x="50" y="61" width="4" height="9"/><rect x="57" y="53" width="4" height="17"/></g>
  </svg>
  <div class="role-name">Hedgefund Partner/CEO</div>
  <p class="role-text">Lorem ipsum dolor sit amet, consectetur adipisicing elit, sed do eiusmod tempor incididunt ut labore et dolore</p>
  <div class="role-btn"></div>
</article>

<article class="abs role-card" style="left:251px">
  <svg width="94" height="108" viewBox="0 0 94 108">
    <polygon points="47,2 92,28 92,80 47,106 2,80 2,28" fill="none" stroke="#444" stroke-width="1"/>
    <g fill="none" stroke="#444" stroke-width="1"><circle cx="50" cy="37" r="10"/><path d="M44,47 L42,53 C36,56 32,60 32,67 L72,67 C72,60 66,56 58,53 L56,47"/></g>
    <circle cx="26" cy="63" r="7" fill="#333"/><text x="26" y="66.5" text-anchor="middle" font-family="Open Sans, sans-serif" font-size="9" font-weight="700" fill="#fff">$</text>
  </svg>
  <div class="role-name">CFO</div>
  <p class="role-text">Lorem ipsum dolor sit amet, consectetur adipisicing elit, sed do eiusmod tempor incididunt ut labore et dolore</p>
  <div class="role-btn">LEARN MORE</div>
</article>

<article class="abs role-card" style="left:420px">
  <svg width="94" height="108" viewBox="0 0 94 108">
    <polygon points="47,2 92,28 92,80 47,106 2,80 2,28" fill="none" stroke="#444" stroke-width="1"/>
    <g fill="none" stroke="#444" stroke-width="1"><circle cx="50" cy="37" r="10"/><path d="M44,47 L42,53 C36,56 32,60 32,67 L72,67 C72,60 66,56 58,53 L56,47"/></g>
    <circle cx="26" cy="63" r="7" fill="#333"/><line x1="23" y1="66" x2="29" y2="60" stroke="#fff" stroke-width="1.6"/>
  </svg>
  <div class="role-name">CTO</div>
  <p class="role-text">Lorem ipsum dolor sit amet, consectetur adipisicing elit, sed do eiusmod tempor incididunt ut labore et dolore</p>
  <div class="role-btn">LEARN MORE</div>
</article>

<article class="abs role-card" style="left:589px">
  <svg width="94" height="108" viewBox="0 0 94 108">
    <polygon points="47,2 92,28 92,80 47,106 2,80 2,28" fill="none" stroke="#444" stroke-width="1"/>
    <g fill="none" stroke="#444" stroke-width="1"><circle cx="50" cy="37" r="10"/><path d="M44,47 L42,53 C36,56 32,60 32,67 L72,67 C72,60 66,56 58,53 L56,47"/></g>
    <circle cx="29" cy="63" r="7" fill="#333"/><line x1="26" y1="66" x2="31" y2="61" stroke="#fff" stroke-width="1.8"/><circle cx="32" cy="60" r="2.2" fill="none" stroke="#fff" stroke-width="1.2"/>
  </svg>
  <div class="role-name">Employee</div>
  <p class="role-text">Lorem ipsum dolor sit amet, consectetur adipisicing elit, sed do eiusmod tempor incididunt ut labore et dolore</p>
  <div class="role-btn">LEARN MORE</div>
</article>

<footer class="abs footer" role="img" aria-label="Black and white photo of a thoughtful business professional"></footer>
<div class="abs footer-brand">Norquell</div>
<ul class="abs footer-links" style="left:187px;top:1001px">
  <li>Home</li><li>About</li><li>Services</li><li>Partners</li><li>Clients</li><li>Contacts</li>
</ul>
<ul class="abs footer-links" style="left:269px;top:1001px">
  <li>Friendloop</li><li>Chirper</li><li>Circleplus</li><li>Workgraph</li>
</ul>
<div class="abs field" style="left:391px;top:1003px;width:173px;height:28px">User</div>
<div class="abs field" style="left:568px;top:1003px;width:173px;height:28px">Email</div>
<div class="abs field" style="left:391px;top:1036px;width:350px;height:54px;padding-top:6px">Comments</div>
<div class="abs btn-send">Send</div>
<div class="abs copyright">© Copyright © 2015, Norquell Inc. All Rights Reserved</div>

</body>
</html>
```